Web Design For Manufacturing And Outsourcing Company

Pick up the pieces from our previous developer and help us complete our website.

5 pages - Home,Machining,Sourcing,About Us, and Contact

Attached you will find screen shots of previous direction but we're open to new ideas.

We can provide all text and images needed.

Thanks!

5+ page

```html
<!DOCTYPE html>
<html lang="en">
<head>
<meta charset="utf-8">
<title>Kestrel Industries</title>
<link href="https://fonts.googleapis.com/css2?family=Lato:wght@400;700&family=Raleway:wght@500;600&display=swap" rel="stylesheet">
<style>
:root{
  --orange:#f26a21;
  --dark:#1c1c1c;
  --black:#0d0d0d;
  --text:#222;
  --muted:#555;
  --card:#f1f1f1;
  --cardline:#cfcfcf;
  --footer:#f1f1f1;
  --blue:#2b6585;
  --white:#fff;
}
*{box-sizing:border-box;margin:0;padding:0}
html,body{width:1200px;height:2647px;overflow:hidden}
body{position:relative;background:var(--white);font-family:"Lato",sans-serif;color:var(--text)}
.abs{position:absolute}
.topline{left:0;top:0;width:1200px;height:5px;background:var(--orange)}
.phone-tab{left:914px;top:0;width:286px;height:50px;background:var(--orange);border-bottom-left-radius:26px;display:flex;align-items:center;padding-left:28px;gap:12px;color:var(--white);font-size:20px}
.phone-tab .ring{width:34px;height:34px;border:2px solid var(--white);border-radius:50%;display:flex;align-items:center;justify-content:center}
.brand{display:flex;align-items:center;gap:12px;font-family:"Raleway",sans-serif;font-weight:600;letter-spacing:5px;white-space:nowrap}
.brand .sq{width:30px;height:30px;background:var(--orange)}
.brand .a{color:var(--dark)}
.brand .b{color:var(--orange)}
.header-brand{left:85px;top:74px;font-size:30px}
.search{left:785px;top:88px;width:329px;height:51px;border:2px solid #ccc;border-radius:4px;display:flex;align-items:center;justify-content:space-between;padding:0 14px;color:#999;font-size:16px}
.nav{left:0;top:176px;width:1200px;height:71px;background:var(--dark);border-bottom:4px solid var(--orange)}
.nav a{position:absolute;top:0;height:67px;line-height:67px;color:var(--white);font-size:16px;text-decoration:none}
.nav .active{left:86px;width:85px;background:var(--orange);text-align:center}
.social{display:flex;gap:10px}
.social span{width:34px;height:34px;border-radius:50%;background:var(--white);display:block}
.nav .social{position:absolute;left:990px;top:16px}
.hero{left:0;top:249px;width:1200px;height:531px;background:linear-gradient(180deg,#5d5d58 0%,#7b7c78 35%,#4a4a46 70%,#2e2e2c 100%)}
.hero-arrow{top:277px;width:38px;height:38px;border:2px solid var(--white);border-radius:50%;display:flex;align-items:center;justify-content:center}
.hero-caption{left:0;top:451px;width:909px;height:80px;background:rgba(30,30,30,.55);color:var(--white);font-family:"Raleway",sans-serif;font-weight:500;font-size:29px;line-height:80px;padding-left:16px;white-space:nowrap}
.card{top:822px;width:247px;height:320px;background:var(--card);border:2px solid var(--cardline);border-radius:4px;text-align:center}
.card .icon{width:113px;height:113px;border-radius:50%;background:var(--orange);margin:12px auto 0;display:flex;align-items:center;justify-content:center}
.card h3{font-family:"Raleway",sans-serif;font-weight:500;font-size:21px;margin-top:22px;color:var(--dark)}
.card p{font-size:13.5px;line-height:20px;margin:10px 22px 0;color:var(--text)}
.about-title{left:85px;top:1190px;font-family:"Raleway",sans-serif;font-weight:500;font-size:25px}
.about-body{left:85px;top:1234px;width:520px;font-size:15.5px;line-height:24px}
.about-body p+p{margin-top:24px}
.btn{left:85px;top:1497px;width:130px;height:42px;background:var(--orange);color:var(--white);font-size:14px;line-height:42px;text-align:center}
.panel{left:715px;top:1197px;width:400px;height:363px;background:var(--card)}
.panel .photo{position:absolute;left:30px;top:28px;width:340px;height:139px;background:linear-gradient(180deg,#3a7bbf 0%,#8fb3d6 55%,#a7c64a 100%)}
.panel h4{position:absolute;left:30px;top:185px;font-family:"Raleway",sans-serif;font-weight:500;font-size:20px}
.panel p{position:absolute;left:30px;top:216px;width:345px;font-size:13.5px;line-height:20px}
.panel .more{position:absolute;left:30px;top:313px;color:var(--orange);font-size:14px}
.panel .pager{position:absolute;left:313px;top:310px;display:flex;gap:16px}
.projects{left:0;top:1617px;width:1200px;height:409px;background:linear-gradient(180deg,#2f6f91,#245b78)}
.projects h2,.clients-title{width:1200px;text-align:center;font-family:"Raleway",sans-serif;font-weight:500;font-size:30px}
.projects h2{position:absolute;top:50px;color:var(--white)}
.proj{top:141px;width:325px;height:201px}
.clients-title{left:0;top:2080px;color:var(--dark)}
.clients{left:85px;top:2164px;width:1030px;height:40px;display:flex;align-items:center;justify-content:space-between}
.client{display:flex;align-items:center;gap:8px;font-weight:700;font-size:19px;color:var(--dark);white-space:nowrap}
.client i{display:block;width:20px;height:20px;background:var(--orange)}
.footer{left:0;top:2268px;width:1200px;height:325px;background:var(--footer)}
.footer-brand{left:85px;top:50px;font-size:21px;letter-spacing:3px;gap:9px}
.footer-brand .sq{width:24px;height:24px}
.footer-about{left:85px;top:94px;width:290px;font-size:15px;line-height:24px}
.fcol h5{font-family:"Raleway",sans-serif;font-weight:500;font-size:20px;color:var(--dark)}
.fcol h5::after{content:"";display:block;width:48px;height:3px;background:var(--orange);margin-top:8px}
.links{list-style:none;margin-top:14px;font-size:13.5px;line-height:30px}
.links li::before{content:"• "}
.fsocial{display:grid;grid-template-columns:repeat(3,34px);gap:10px;margin-top:20px}
.fsocial span{width:34px;height:34px;border-radius:50%;background:#aaa;display:block}
.contact-row{display:flex;gap:14px;font-size:13.5px;line-height:24px;margin-top:18px}
.contact-row svg{flex:none;margin-top:4px}
.bottom{left:0;top:2593px;width:1200px;height:54px;background:var(--black);color:var(--white);font-size:14px;line-height:54px;padding-left:88px}
.bottom b{color:var(--orange);font-weight:400}
</style>
</head>
<body>
<div class="abs topline"></div>
<div class="abs phone-tab">
  <span class="ring"><svg width="18" height="18" viewBox="0 0 24 24"><path d="M6.6 10.8a15 15 0 0 0 6.6 6.6l2.2-2.2a1 1 0 0 1 1-.25 11 11 0 0 0 3.6.6 1 1 0 0 1 1 1V20a1 1 0 0 1-1 1A17 17 0 0 1 3 4a1 1 0 0 1 1-1h3.5a1 1 0 0 1 1 1 11 11 0 0 0 .6 3.6 1 1 0 0 1-.25 1z" fill="#fff"/></svg></span>
  (555) 010-2040
</div>
<div class="abs brand header-brand"><span class="sq"></span><span class="a">KESTREL</span><span class="b">INDUSTRIES</span></div>
<div class="abs search">Search<svg width="22" height="22" viewBox="0 0 24 24"><circle cx="10" cy="10" r="7" fill="none" stroke="#aaa" stroke-width="2"/><path d="M15 15l6 6" stroke="#aaa" stroke-width="2"/></svg></div>

<nav class="abs nav">
  <a class="active" href="#">HOME</a>
  <a href="#" style="left:233px">MACHINING</a>
  <a href="#" style="left:406px">SOURCING</a>
  <a href="#" style="left:570px">ABOUT US</a>
  <a href="#" style="left:732px">CONTACT</a>
  <div class="social" aria-label="Social links"><span></span><span></span><span></span></div>
</nav>

<section class="abs hero" role="img" aria-label="Photo of an industrial plant floor with machinery and ducting">
  <div class="abs hero-arrow" style="left:16px"><svg width="14" height="14" viewBox="0 0 14 14"><path d="M9 2L4 7l5 5" fill="none" stroke="#fff" stroke-width="2"/></svg></div>
  <div class="abs hero-arrow" style="left:1144px"><svg width="14" height="14" viewBox="0 0 14 14"><path d="M5 2l5 5-5 5" fill="none" stroke="#fff" stroke-width="2"/></svg></div>
  <div class="abs hero-caption">WE ARE SERVING INDUSTRIAL AND COMMERCIAL SECTORS</div>
</section>

<div class="abs card" style="left:85px">
  <div class="icon"><svg width="56" height="64" viewBox="0 0 24 28"><path d="M15 1L4 16h7l-3 11 12-16h-7z" fill="#fff"/></svg></div>
  <h3>ELECTRICAL</h3>
  <p>Lorem Ipsum is simply dummy text of the printing and typesetting industry. Lorem Ipsum has been the industry's standard dummy text</p>
</div>
<div class="abs card" style="left:346px">
  <div class="icon"><svg width="66" height="66" viewBox="0 0 24 24"><path d="M10 1h4l.6 3 2.3 1 2.6-1.7 2.8 2.8-1.7 2.6 1 2.3 3 .6v4l-3 .6-1 2.3 1.7 2.6-2.8 2.8-2.6-1.7-2.3 1-.6 3h-4l-.6-3-2.3-1-2.6 1.7-2.8-2.8 1.7-2.6-1-2.3-3-.6v-4l3-.6 1-2.3L2.7 6.1 5.5 3.3l2.6 1.7 2.3-1z" fill="#fff"/><circle cx="12" cy="12" r="4" fill="#f26a21"/></svg></div>
  <h3>AUTOMATION</h3>
  <p>Lorem Ipsum is simply dummy text of the printing and typesetting industry. Lorem Ipsum has been the industry's standard dummy text</p>
</div>
<div class="abs card" style="left:607px">
  <div class="icon"><svg width="64" height="64" viewBox="0 0 24 24"><path d="M4 20L14 10" stroke="#fff" stroke-width="3.5" stroke-linecap="round"/><circle cx="16" cy="8" r="4.5" fill="#fff"/><circle cx="17.5" cy="6.5" r="2" fill="#f26a21"/><path d="M20 20L9 9" stroke="#fff" stroke-width="3" stroke-linecap="round"/><rect x="3" y="4" width="8" height="4" transform="rotate(45 7 6)" fill="#fff"/></svg></div>
  <h3>MILLWRIGHT</h3>
  <p>Lorem Ipsum is simply dummy text of the printing and typesetting industry. Lorem Ipsum has been the industry's standard dummy text</p>
</div>
<div class="abs card" style="left:868px">
  <div class="icon"><svg width="60" height="60" viewBox="0 0 24 24"><path d="M12 2l1.8 6.2L20 6l-4 5 6 1-6 1.5 4 5.5-6.2-3L12 22l-1.8-6-6.2 3 4-5.5L2 12l6-1-4-5 6.2 2.2z" fill="#fff"/></svg></div>
  <h3>FABRICATION</h3>
  <p>Lorem Ipsum is simply dummy text of the printing and typesetting industry. Lorem Ipsum has been the industry's standard dummy text</p>
</div>

<h2 class="abs about-title">ABOUT KESTREL INDUSTRIES</h2>
<div class="abs about-body">
  <p>Lorem Ipsum is simply dummy text of the printing and typesetting industry. Lorem Ipsum has been the industry's standard dummy text ever since the 1500s, when an unknown printer took a galley of type and scrambled it to make a type specimen book.</p>
  <p>It has survived not only five centuries, but also the leap into electronic typesetting, remaining essentially unchanged. It was popularised in the 1960s with the release of Letraset sheets containing Lorem Ipsum passages, and more recently with desktop publishing software like Aldus PageMaker including versions of Lorem Ipsum.</p>
</div>
<div class="abs btn">READ MORE</div>

<aside class="abs panel">
  <div class="photo" role="img" aria-label="Photo of a worker in a hard hat and safety vest with a laptop near power lines"></div>
  <h4>WORK EXPERIENCE</h4>
  <p>Lorem Ipsum is simply dummy text of the printing and typesetting industry.<br>Lorem Ipsum has been the industry's standard dummy text ever since the 1500s.</p>
  <div class="more">READ MORE ▸</div>
  <div class="pager"><svg width="14" height="16" viewBox="0 0 14 16"><path d="M10 2L4 8l6 6" fill="none" stroke="#222" stroke-width="2"/></svg><svg width="14" height="16" viewBox="0 0 14 16"><path d="M4 2l6 6-6 6" fill="none" stroke="#222" stroke-width="2"/></svg></div>
</aside>

<section class="abs projects">
  <h2>OUR PROJECTS</h2>
  <div class="abs proj" style="left:79px;background:linear-gradient(135deg,#9aa5ad,#dfe5ea 50%,#7f8b93)" role="img" aria-label="Photo of a milling cutter spraying coolant on metal"></div>
  <div class="abs proj" style="left:439px;background:linear-gradient(135deg,#1d2a6b,#5d6a9c 50%,#1a1d3a)" role="img" aria-label="Photo of a machined metal block in a vise"></div>
  <div class="abs proj" style="left:796px;background:linear-gradient(135deg,#8e9298,#d7d9dc 50%,#9ea2a7)" role="img" aria-label="Photo of machined steel parts on technical drawings"></div>
</section>

<h2 class="abs clients-title">OUR CLIENTS</h2>
<div class="abs clients">
  <div class="client"><i></i>Alpstead</div>
  <div class="client">Orbis Group</div>
  <div class="client">Northgate College</div>
  <div class="client"><i></i>Maple Kibble Co.</div>
  <div class="client">Prairie Grain</div>
  <div class="client">Veltmann</div>
</div>

<footer class="abs footer">
  <div class="abs brand footer-brand"><span class="sq"></span><span class="a">KESTREL</span><span class="b">INDUSTRIES</span></div>
  <p class="abs footer-about">Lorem Ipsum is simply dummy text of the printing and typesetting industry. Lorem Ipsum has been the industry's standard dummy text ever since the 1500s, when an unknown printer took a galley of type and scrambled it to make a type specimen book.</p>
  <div class="abs fcol" style="left:455px;top:44px">
    <h5>SITE LINKS</h5>
    <ul class="links"><li>HOME</li><li>SERVICES</li><li>PROJECTS</li><li>ABOUT US</li><li>CAREERS</li><li>CONTACT US</li></ul>
  </div>
  <div class="abs fcol" style="left:681px;top:44px">
    <h5>FOLLOW US</h5>
    <div class="fsocial" aria-label="Social links"><span></span><span></span><span></span><span></span><span></span><span></span></div>
  </div>
  <div class="abs fcol" style="left:902px;top:44px">
    <h5>CONTACT US</h5>
    <div class="contact-row"><svg width="14" height="18" viewBox="0 0 14 18"><path d="M7 0a7 7 0 0 0-7 7c0 5 7 11 7 11s7-6 7-11a7 7 0 0 0-7-7z" fill="#f26a21"/><circle cx="7" cy="7" r="2.5" fill="#f1f1f1"/></svg><span>123 Street Name, City Name<br>Country Name</span></div>
    <div class="contact-row" style="margin-top:26px"><svg width="16" height="16" viewBox="0 0 24 24"><path d="M6.6 10.8a15 15 0 0 0 6.6 6.6l2.2-2.2a1 1 0 0 1 1-.25 11 11 0 0 0 3.6.6 1 1 0 0 1 1 1V20a1 1 0 0 1-1 1A17 17 0 0 1 3 4a1 1 0 0 1 1-1h3.5a1 1 0 0 1 1 1 11 11 0 0 0 .6 3.6 1 1 0 0 1-.25 1z" fill="#f26a21"/></svg><span>09 555 0142</span></div>
    <div class="contact-row" style="margin-top:26px"><svg width="16" height="14" viewBox="0 0 16 12"><rect width="16" height="12" fill="#f26a21"/><path d="M0 0l8 6 8-6" fill="none" stroke="#f1f1f1" stroke-width="1.5"/></svg><span>info@domain.com</span></div>
  </div>
</footer>
<div class="abs bottom">© 2019 <b>kestrel industries</b> | All rights reserved.</div>
</body>
</html>
```